Design for online reviews widget

Attached is a wireframe of a widget we need designing to display reviews on websites from multiple sources. We need this provided at 3 different sizes including full screen, contained (like the wireframe) and mobile.
You have completely free rein on the styling.
The only elements that should remain untouched are the blue stars (https://www.filevault-demo.net/s/8pwtmz2lq4nv90h/kt%20stars.ai?dl=0) and powered by logo at the bottom.
Ignore the menu at the top of the wireframe, this is just from the website the widget will be placed on.
Target Market(s)
Businesses
Look and feel
Each slider illustrates characteristics of the customer's brand and the style your logo design should communicate.

```html
<!DOCTYPE html>
<html lang="en">
<head>
<meta charset="utf-8">
<title>Review Widget</title>
<link href="https://fonts.googleapis.com/css2?family=Lexend:wght@500;600&family=Arimo:wght@400;700&display=swap" rel="stylesheet">
<style>
  :root {
    --bg: #e6f8fd;
    --card: #f6fcff;
    --accent: #3dbfe8;
    --ink: #111111;
    --green: #4f9d2b;
    --gold: #f5b82e;
    --trades: #e3252c;
    --search: #3f7fe6;
    --trust: #0f1d3a;
    --trust-dot: #1fb879;
    --dial: #f2cf1b;
    --ring: #1958a8;
  }
  * { box-sizing: border-box; margin: 0; padding: 0; }
  html, body { width: 1200px; height: 942px; overflow: hidden; }
  body {
    position: relative;
    background: var(--bg);
    font-family: "Arimo", Arial, sans-serif;
    color: var(--ink);
    border-top: 4px solid #b8ecfb;
  }
  .score-stars {
    position: absolute; left: 522px; top: 30px;
    display: flex; gap: 5px;
  }
  .score-stars svg { width: 33px; height: 33px; }
  .score-label {
    position: absolute; left: 0; width: 1236px; top: 69px;
    text-align: center; font-family: "Lexend", sans-serif; font-weight: 500;
    font-size: 12.5px;
  }
  .filter {
    position: absolute; left: 968px; top: 68px; width: 113px; height: 19px;
    background: #fff; border-radius: 6px; font-size: 10px;
    display: flex; align-items: center; justify-content: space-between;
    padding: 0 8px 0 12px;
  }
  .filter svg { width: 7px; height: 5px; }
  .card {
    position: absolute; width: 314px;
    background: var(--card); border-radius: 8px;
    padding: 28px 10px 16px 22px;
    border-bottom: 4px solid var(--accent);
    box-shadow: 0 1px 3px rgba(0,0,0,0.03);
  }
  .tab {
    position: absolute; left: 18px; background: #fff;
    padding: 4px 7px; display: flex; gap: 1px;
  }
  .tab svg { width: 14px; height: 14px; }
  .ring {
    position: absolute; left: 24px; top: -22px;
    width: 45px; height: 45px; border-radius: 50%;
    border: 2px solid var(--ring); background: #fff;
    display: flex; align-items: center; justify-content: center;
  }
  .ring span { width: 37px; height: 37px; border-radius: 50%; background: var(--ring); display: block; }
  .brand {
    height: 22px; display: flex; align-items: center; gap: 5px;
    font-family: "Lexend", sans-serif; font-weight: 500; font-size: 16px;
  }
  .brand.trades { color: var(--trades); }
  .brand.search { color: var(--search); font-size: 19px; }
  .brand.trust { color: var(--trust); }
  .brand.trust .mark { width: 12px; height: 12px; background: var(--trust-dot); }
  .brand.dial { color: var(--ink); font-size: 18px; }
  .brand.dial .mark { width: 18px; height: 18px; background: var(--dial); }
  .title {
    margin-top: 10px; font-family: "Lexend", sans-serif; font-weight: 500;
    font-size: 16px; line-height: 19px;
  }
  .body { margin-top: 14px; font-size: 10px; line-height: 14.4px; }
  .body.tight { line-height: 11.5px; }
  .meta { margin-top: 14px; font-size: 10px; line-height: 14.4px; font-weight: 700; }
  .by { margin-top: 13px; font-size: 10px; line-height: 12px; color: var(--green); }
  .load {
    position: absolute; left: 527px; top: 771px; width: 146px; height: 41px;
    background: var(--accent); color: #fff; border-radius: 21px;
    font-family: "Lexend", sans-serif; font-weight: 600; font-size: 15px;
    display: flex; align-items: center; justify-content: center; letter-spacing: 0.5px;
  }
  .powered {
    position: absolute; left: 922px; top: 845px; width: 176px; text-align: right;
  }
  .powered small { display: block; font-size: 12px; margin-right: 52px; }
  .powered .name {
    display: flex; align-items: center; justify-content: flex-end; gap: 8px;
    font-family: "Lexend", sans-serif; font-weight: 600; font-size: 21px; margin-top: 4px;
  }
  .powered .dot { width: 30px; height: 30px; border-radius: 50%; background: var(--accent); }
  .powered .tag { font-size: 6px; letter-spacing: 3px; color: #555; margin-top: 1px; }
</style>
</head>
<body>
<svg width="0" height="0" style="position:absolute">
  <defs>
    <symbol id="star" viewBox="0 0 24 24"><path d="M12 2l2.9 6.3 6.9.7-5.2 4.6 1.5 6.8L12 17l-6.1 3.4 1.5-6.8L2.2 9l6.9-.7z"/></symbol>
    <symbol id="round-star" viewBox="0 0 34 34"><circle cx="17" cy="17" r="17" fill="#3dbfe8"/><circle cx="17" cy="17" r="12" fill="none" stroke="#fff" stroke-width="1.6"/><use href="#star" x="9" y="8.5" width="16" height="16" fill="#fff"/></symbol>
  </defs>
</svg>

<div class="score-stars">
  <svg><use href="#round-star"/></svg><svg><use href="#round-star"/></svg><svg><use href="#round-star"/></svg><svg><use href="#round-star"/></svg><svg><use href="#round-star"/></svg>
</div>
<div class="score-label">Combined Review Score 4.3 out of 5</div>
<div class="filter">Filter Results <svg viewBox="0 0 8 6"><path d="M0 0h8L4 6z" fill="#3dbfe8"/></svg></div>

<!-- column 1 -->
<div class="card" style="left:103px; top:143px; min-height:288px;">
  <div class="ring"><span></span></div>
  <div class="brand trades">Vetted Trades</div>
  <div class="title">Front door with windows each<br>side and side window</div>
  <div class="body">This is the second time we have used meridian home Improvments , and the service is amazing! Owen came round several times as we keep changing our minds and he was so helpful and gave us good advice, and the guys who do the fitting are efficient and tidy . I've got to say the end result is amazing and I have recommended to many of friends . Thanks Meridian</div>
  <div class="meta">Reliablity: 9.38 Courtesy: 10 Tidiness: 9.84<br>Workmanship: 10</div>
  <div class="by">Verified 28th September 2021 | Located in Ashford</div>
</div>

<div class="card" style="left:105px; top:465px; min-height:253px;">
  <div class="tab" style="top:-9px;"><svg fill="var(--gold)"><use href="#star"/></svg><svg fill="var(--gold)"><use href="#star"/></svg><svg fill="var(--gold)"><use href="#star"/></svg><svg fill="var(--gold)"><use href="#star"/></svg><svg fill="var(--gold)"><use href="#star"/></svg></div>
  <div class="brand dial"><span class="mark"></span>Dialbook</div>
  <div class="title">Brilliant all round professional,<br>friendly service.</div>
  <div class="body tight">This home run friendly business was a real pleasure to deal with. From the professional, no pressure quote, nothing was too much trouble to ensure everything is as required for your needs with the quote and fitting. The workmanship and double glazing being fitted was brilliant and my home/outdoors was left tidy and clean leaving an outstanding impression for such an all round professional job. I would not hesitate to recommend this company, such a brilliant service from great hardworking people that care about their service.</div>
  <div class="by">13 Feb 2018 by GreenChair42</div>
</div>

<!-- column 2 -->
<div class="card" style="left:444px; top:130px; min-height:259px;">
  <div class="tab" style="top:-9px;"><svg fill="var(--gold)"><use href="#star"/></svg><svg fill="var(--gold)"><use href="#star"/></svg><svg fill="var(--gold)"><use href="#star"/></svg><svg fill="var(--gold)"><use href="#star"/></svg><svg fill="var(--gold)"><use href="#star"/></svg></div>
  <div class="brand search">Searchly</div>
  <div class="title">Positive: Professionalism,<br>Quality, Value</div>
  <div class="body tight">The team did a good job of replacing a large feature window spanning two floors, as well as the others in my property. They're a professional group who were willing to work out solutions to any problem, especially compared to other companies. Prices are fair, and my new UPVC windows look great. Special thanks to Frank for being so accommodating and for the good communication throughout.</div>
  <div class="meta">Service: Window installation</div>
  <div class="by">11 months ago by Daniel Hart</div>
</div>

<div class="card" style="left:444px; top:429px; min-height:289px;">
  <div class="ring"><span></span></div>
  <div class="brand trades">Vetted Trades</div>
  <div class="title">Front door with windows each<br>side and side window</div>
  <div class="body">This is the second time we have used meridian home Improvments , and the service is amazing! Owen came round several times as we keep changing our minds and he was so helpful and gave us good advice, and the guys who do the fitting are efficient and tidy . I've got to say the end result is amazing and I have recommended to many of friends . Thanks Meridian</div>
  <div class="meta">Reliablity: 9.38 Courtesy: 10 Tidiness: 9.84<br>Workmanship: 10</div>
  <div class="by">Verified 28th September 2021 | Located in Ashford</div>
</div>

<!-- column 3 -->
<div class="card" style="left:782px; top:137px; min-height:223px;">
  <div class="tab" style="top:-16px;"><svg fill="var(--trust-dot)"><use href="#star"/></svg><svg fill="var(--trust-dot)"><use href="#star"/></svg><svg fill="var(--trust-dot)"><use href="#star"/></svg><svg fill="var(--trust-dot)"><use href="#star"/></svg><svg fill="var(--trust-dot)"><use href="#star"/></svg></div>
  <div class="brand trust"><span class="mark"></span>TrustMeter</div>
  <div class="title">Front door with windows each<br>side and side window</div>
  <div class="body tight">This is the second time we have used meridian home Improvments , and the service is amazing! Owen came round several times as we keep changing our minds and he was so helpful and gave us good advice, and the guys who do the fitting are efficient and tidy . I've got to say the end result is amazing and I have recommended to many of friends . Thanks Meridian</div>
  <div class="by">13 Feb 2018 by Jo</div>
</div>

<div class="card" style="left:782px; top:395px; min-height:259px;">
  <div class="tab" style="top:-9px;"><svg fill="var(--gold)"><use href="#star"/></svg><svg fill="var(--gold)"><use href="#star"/></svg><svg fill="var(--gold)"><use href="#star"/></svg><svg fill="var(--gold)"><use href="#star"/></svg><svg fill="var(--gold)"><use href="#star"/></svg></div>
  <div class="brand search">Searchly</div>
  <div class="title">Positive: Professionalism,<br>Quality, Value</div>
  <div class="body tight">The team did a good job of replacing a large feature window spanning two floors, as well as the others in my property. They're a professional group who were willing to work out solutions to any problem, especially compared to other companies. Prices are fair, and my new UPVC windows look great. Special thanks to Frank for being so accommodating and for the good communication throughout.</div>
  <div class="meta">Service: Window installation</div>
  <div class="by">11 months ago by Daniel Hart</div>
</div>

<div class="load">LOAD MORE</div>

<div class="powered">
  <small>Powered by</small>
  <div class="name"><span class="dot"></span>ReviewWeave</div>
  <div class="tag">REVIEW AGGREGATION</div>
</div>
</body>
</html>
```